Stylish Business Cards Wanted

- DOUBLE SIDED Design Required -

High end, edgy cards for a corporate and personal stylist. Must include logo,
Name: Belinda Marsh
Title: Director and Stylist
telephone : +61 8 8417 2950
email: belinda@thewardrobeledger.com
website: thewardrobeledger.com
Tag: Corporate Workwear & Uniform Specialist | Personal Stylist
Would like nice icons for telephone, email, website

Target Market(s)

Businesses wanting stylish uniforms, people wanting stylish wardrobes

Industry/Entity Type

Corporate Workwear Stylist

Contact Information for Business Card

I would like black, white and gold foiling incorporated in the design - possibly a touch of the other colours on my branding guide attached Name: Belinda Marsh Title: Director and Stylist telephone : +61 8 8417 2950 email: belinda@thewardrobeledger.com website: thewardrobeledger.com Tag: Corporate Workwear & Uniform Specialist | Personal Stylist Would like nice icons for telephone, email, website

Font styles to use
Other font styles liked:
• Raleway

Colors

Designer to choose colors to be used in the design.

Requirements
Must have
• Gold foil accents

```html
<!DOCTYPE html>
<html lang="en">
<head>
<meta charset="utf-8">
<title>The Wardrobe Ledger – Business Cards</title>
<link href="https://fonts.googleapis.com/css2?family=Raleway:wght@400;500;600&display=swap" rel="stylesheet">
<style>
  :root {
    --paper-bg: #d9d9d9;
    --card-black: #1e1e1e;
    --card-white: #f7f7f5;
    --gold: #d9b142;
    --gold-deep: #b8902a;
    --ink: #1b1b1b;
    --light-text: #f2f2f2;
  }
  * { margin: 0; padding: 0; box-sizing: border-box; }
  html, body { width: 1200px; height: 800px; overflow: hidden; }
  body {
    background: var(--paper-bg);
    font-family: "Raleway", sans-serif;
    position: relative;
  }
  .card {
    position: absolute;
    top: 245px;
    width: 540px;
    height: 310px;
    overflow: hidden;
  }
  .card-front { left: 45px; background: var(--card-white); }
  .card-back { left: 615px; background: var(--card-black); border-bottom: 5px solid var(--gold); }

  .contact-panel {
    position: absolute; left: 0; top: 0;
    width: 250px; height: 100%;
    background: var(--card-black);
  }
  .person-name {
    position: absolute; left: 30px; top: 62px;
    color: var(--light-text);
    font-weight: 600; font-size: 19px; letter-spacing: 0.5px;
    text-transform: uppercase;
  }
  .person-title {
    position: absolute; left: 30px; top: 88px;
    color: var(--gold); font-size: 13px; font-weight: 500;
  }
  .contact-list {
    position: absolute; left: 30px; top: 118px;
    list-style: none;
  }
  .contact-list li {
    display: flex; align-items: center; gap: 8px;
    color: var(--light-text); font-size: 11.5px; line-height: 19px;
  }
  .contact-list svg { width: 11px; height: 11px; flex: none; }
  .social-row {
    position: absolute; left: 30px; top: 190px;
    display: flex; gap: 5px;
  }
  .social-dot {
    width: 17px; height: 17px; border-radius: 50%;
    border: 1.5px solid var(--gold);
  }

  .brand-lockup {
    position: absolute; left: 250px; top: 0;
    width: 290px; height: 245px;
    display: flex; align-items: center; justify-content: center;
  }
  .brand-name {
    font-weight: 600; font-size: 24px; color: var(--ink);
    letter-spacing: 1px; text-align: center; line-height: 1.25;
  }

  .tagline-band {
    position: absolute; left: 0; top: 245px;
    width: 100%; height: 30px;
    background: var(--gold);
    display: flex; align-items: center; justify-content: center;
    color: var(--ink); font-size: 11px; font-weight: 500;
    letter-spacing: 1.6px; text-transform: uppercase;
  }

  .back-brand {
    position: absolute; inset: 0;
    display: flex; align-items: center; justify-content: center;
  }
  .back-brand .brand-name {
    color: var(--gold); font-size: 36px;
  }
</style>
</head>
<body>

<section class="card card-front">
  <div class="contact-panel">
    <p class="person-name">Belinda Marsh</p>
    <p class="person-title">Director &amp; Stylist</p>
    <ul class="contact-list">
      <li>
        <svg viewBox="0 0 12 12"><path d="M2.5 1 L4.5 1 L5.2 3.4 L4 4.3 C4.7 5.8 6 7.2 7.7 8 L8.6 6.8 L11 7.5 L11 9.5 C11 10.3 10.3 11 9.5 11 C5 11 1 7 1 2.5 C1 1.7 1.7 1 2.5 1 Z" fill="#d9b142"/></svg>
        +61 8 8417 2950
      </li>
      <li>
        <svg viewBox="0 0 12 12"><rect x="0.5" y="2" width="11" height="8" fill="#d9b142"/><path d="M0.5 2 L6 6.5 L11.5 2" fill="none" stroke="#1e1e1e" stroke-width="1"/></svg>
        belinda@thewardrobeledger.com
      </li>
      <li>
        <svg viewBox="0 0 12 12"><circle cx="6" cy="6" r="5" fill="none" stroke="#d9b142" stroke-width="1.2"/><ellipse cx="6" cy="6" rx="2.2" ry="5" fill="none" stroke="#d9b142" stroke-width="1"/><line x1="1" y1="6" x2="11" y2="6" stroke="#d9b142" stroke-width="1"/></svg>
        thewardrobeledger.com
      </li>
    </ul>
    <div class="social-row" aria-label="Social profiles">
      <span class="social-dot"></span>
      <span class="social-dot"></span>
      <span class="social-dot"></span>
    </div>
  </div>

  <div class="brand-lockup">
    <p class="brand-name">The Wardrobe Ledger</p>
  </div>

  <div class="tagline-band">Corporate Workwear | Uniform Specialist | Personal Stylist</div>
</section>

<section class="card card-back">
  <div class="back-brand">
    <p class="brand-name">The Wardrobe Ledger</p>
  </div>
</section>

</body>
</html>
```